Marisa Dee Creations & Affairs business card

I need an elegant informative but not busy business card using my logo. We are a florist with high end customers. I am adding a PDF file and a PNG file for those who requested it

Reason: still working on changes

Reason: Working on changes

Reason: making changes

Target Market(s)

Brides, grooms, men purchasing flowers
Ages 20-65

Industry/Entity Type

Florist

Requirements
Must have
• Business info:
Marisa Dee Creation & Affairs
www.marisadeeaffairs.example.
555-418-7362

555-418-7362
Nice to have
• Est 1954
may want Pinterest logo, twitter and linkedin and facbook
Should not have
• Clip art or photos

```html
<!DOCTYPE html>
<html lang="en">
<head>
<meta charset="utf-8">
<title>Marisa Dee Creations &amp; Affairs – Business Card</title>
<link rel="stylesheet" href="https://fonts.googleapis.com/css2?family=Cinzel:wght@400&family=Montserrat:wght@400&display=swap">
<style>
  :root {
    --stage: #2b2b2d;
    --card-dark: #1f1c1d;
    --card-dark-soft: #2a2627;
    --panel: #ffffff;
    --panel-shade: #ececec;
    --ink: #1a1a1a;
    --ink-grey: #6e6e6e;
    --blush: #e3a3ac;
  }
  * { box-sizing: border-box; margin: 0; padding: 0; }
  html, body { width: 1200px; height: 900px; overflow: hidden; }
  body {
    background: var(--stage);
    display: flex;
    flex-direction: column;
    align-items: center;
    justify-content: center;
    gap: 46px;
  }
  .card {
    position: relative;
    width: 660px;
    height: 377px;
    overflow: hidden;
    background: var(--card-dark);
    box-shadow: 0 12px 30px rgba(0,0,0,.45);
  }
  .damask {
    position: absolute;
    inset: 0;
    background: radial-gradient(ellipse at 30% 40%, var(--card-dark-soft), var(--card-dark) 70%);
  }

  /* Front */
  .front-panel {
    position: absolute;
    top: 0; bottom: 0;
    left: 222px;
    width: 258px;
    background: linear-gradient(135deg, var(--panel), var(--panel-shade));
    display: flex;
    flex-direction: column;
    align-items: center;
    justify-content: center;
  }
  .brand-dot {
    width: 34px; height: 34px;
    border-radius: 50%;
    background: var(--blush);
    margin-bottom: 16px;
  }
  .brand-name {
    font-family: "Cinzel", serif;
    font-size: 30px;
    letter-spacing: 2px;
    color: var(--ink);
    line-height: 1;
  }
  .brand-tagline {
    font-family: "Montserrat", sans-serif;
    font-size: 8.5px;
    letter-spacing: 3px;
    color: var(--blush);
    text-transform: uppercase;
    margin-top: 7px;
  }

  /* Back */
  .back-band {
    position: absolute;
    left: 0; right: 0;
    top: 124px;
    height: 100px;
    background: var(--panel);
    display: flex;
    flex-direction: column;
    align-items: center;
    justify-content: center;
    gap: 6px;
  }
  .contact-line {
    font-family: "Cinzel", serif;
    font-size: 24px;
    color: var(--ink-grey);
    letter-spacing: 1px;
    line-height: 1.1;
  }
  .contact-web { text-transform: uppercase; }
</style>
</head>
<body>
  <section class="card card-front">
    <div class="damask" role="img" aria-label="Dark tone-on-tone floral damask pattern"></div>
    <div class="front-panel">
      <span class="brand-dot"></span>
      <div class="brand-name">Marisa Dee</div>
      <div class="brand-tagline">Creations &amp; Affairs</div>
    </div>
  </section>

  <section class="card card-back">
    <div class="damask" role="img" aria-label="Dark tone-on-tone floral damask pattern"></div>
    <div class="back-band">
      <div class="contact-line contact-web">www.marisadeeaffairs.example</div>
      <div class="contact-line contact-phone">555-418-7362</div>
    </div>
  </section>
</body>
</html>
```